Web design for a dental and eye clinic

We need a web design for a dental and eye clinic ( with medical laboratory services) with two branches in Lagos Nigeria. The ultimate aim is to attract more patronage. The design should have links to social media and should have provision for appointments and enquiries. Blue should be part of the colours

Name of facility. VORANTACARE Added Saturday, May 27, 2017

Target Market(s)

Lagos. Nigeria

Industry/Entity Type

Health Care

Number of Pages Required

3 page

Font styles to use
Sans Serif

Colors
85cae6
cadf82

Requirements
Must have
• a projection of the professioal services rendered
Nice to have
• portal for enquiries and appointments
• Link to our facebook, twitter and instagram

```html
<!DOCTYPE html>
<html lang="en">
<head>
<meta charset="utf-8">
<title>Vorantacare – Dental, Eye &amp; Laboratory Clinic</title>
<link href="https://fonts.googleapis.com/css2?family=Varela+Round&family=Open+Sans:wght@400;600;700&family=PT+Serif:ital@0;1&display=swap" rel="stylesheet">
<style>
:root{
  --backdrop:#c9c9c9;
  --blue:#1aaed6;
  --blue-dark:#1697bd;
  --sky:#85cae6;
  --green:#cadf82;
  --green-deep:#9fbf4a;
  --slate:#4b5f6f;
  --slate-light:#5b6e7d;
  --ink:#3a3f44;
  --muted:#8a9097;
  --line:#e3e6e8;
  --panel:#f3f3f3;
  --white:#ffffff;
}
*{margin:0;padding:0;box-sizing:border-box}
html,body{width:960px;height:1200px;overflow:hidden;background:var(--backdrop)}
body{font-family:"Open Sans",sans-serif;color:var(--ink)}
.stage{position:absolute;left:0;top:0;width:1200px;height:1500px;transform:scale(.8);transform-origin:0 0}
.page{position:absolute;left:331px;top:0;width:549px;height:1500px;background:var(--white);overflow:hidden}
.a{position:absolute}
.heading{font-family:"Varela Round",sans-serif;font-weight:400;color:var(--ink)}
.serif{font-family:"PT Serif",serif}
.tiny{font-size:5px;line-height:1.55}

/* top bar */
.topbar{left:0;top:0;width:549px;height:17px;border-bottom:1px solid var(--line);font-size:5px}
.topbar .city{left:36px;top:5px;font-weight:700;color:var(--ink)}
.topbar .link{top:5px;color:var(--muted)}
.topbar .soc{top:5px;width:6px;height:6px;border-radius:50%;background:#9aa1a7}
.topbar .search{left:403px;top:0;width:113px;height:17px;border-left:1px solid var(--line);border-right:1px solid var(--line);padding:5px 9px;color:var(--muted)}

/* header */
.brand{left:41px;top:30px;display:flex;align-items:center;gap:4px}
.brand-name{font-family:"Open Sans",sans-serif;font-weight:700;font-size:11px;letter-spacing:.3px;color:var(--blue-dark)}
.brand-mark{width:8px;height:8px;background:var(--green-deep)}
.nav{top:37px;font-size:5px;font-weight:700;color:var(--ink)}
.nav.on{color:var(--blue)}

/* info bar */
.infobar{left:0;top:62px;width:549px;height:31px;background:var(--panel)}
.infobar .t{font-size:5px;font-weight:700}
.infobar .s{font-size:4.5px;color:var(--muted)}
.appt{left:395px;top:62px;width:121px;height:31px;background:var(--blue);color:var(--white)}

/* hero */
.hero{left:0;top:93px;width:549px;height:232px;background:linear-gradient(100deg,#3f8fb5 0%,#6fb6d8 35%,#bfe0ee 62%,#e4eed2 100%)}
.hero-title{left:80px;top:148px;color:var(--white);font-size:16px}
.hero-sub{left:80px;top:170px;color:var(--white);font-size:18px;font-style:italic}
.hero-text{left:80px;top:201px;width:170px;color:#eaf6fb;font-size:6px;line-height:1.5}
.hero-btn{left:80px;top:240px;width:90px;height:17px;border-radius:9px;background:var(--green);color:var(--ink);font-size:5.5px;font-weight:600;text-align:center;line-height:17px}
.arrow{top:194px;width:33px;height:28px;background:var(--blue)}
.gear{left:0;top:111px;width:17px;height:17px;background:var(--blue)}

/* service tiles */
.tile{top:289px;height:71px;color:var(--white);padding:20px 0 0 17px}
.tile h3{font-size:7.5px;font-weight:700;margin-bottom:5px}
.tile p{font-size:6px;line-height:1.5;width:88px}
.tile svg{position:absolute;right:18px;top:14px}
.tile.green{color:var(--ink)}

/* about */
.about-title{left:36px;top:378px;font-size:18px}
.about-sub{left:36px;top:407px;font-size:11px;font-style:italic;color:#a8adb2}
.photo{left:36px;top:435px;width:130px;height:73px;background:linear-gradient(120deg,#7ea7c4,#cfdde8 55%,#3f6f9b)}
.caption{left:36px;top:514px;width:60px;color:#a5aab0}
.about-text{left:179px;top:432px;width:188px;font-size:6.5px;line-height:1.65;color:#6b7177}
.about-text p{margin-bottom:4px}
.cert-panel{left:406px;top:360px;width:110px;height:212px;background:var(--panel)}
.cert-panel h4{font-size:6.5px;font-weight:600;text-align:center;margin-top:18px;line-height:1.35}
.cert{left:27px;width:57px;height:37px;border:1px solid #b9bdc1;background:#e9e4d4}
.dot{left:94px;width:7px;height:7px;border:1px solid #b4b9be;border-radius:50%}

/* advantages */
.adv{left:0;top:572px;width:549px;height:194px;background:var(--blue);color:var(--white)}
.adv-title{left:36px;top:22px;font-size:17px;color:var(--white)}
.adv-col{top:68px;width:112px}
.adv-col svg{display:block;height:24px}
.adv-col h4{font-family:"Varela Round",sans-serif;font-weight:400;font-size:9.5px;line-height:1.15;margin:12px 0 10px}
.adv-col p{font-size:5.5px;line-height:1.6;color:#d5f0f8}

/* stats */
.stats{left:0;top:766px;width:549px;height:58px;background:var(--slate);color:var(--white)}
.num{top:18px;font-size:17px;font-weight:700}
.lab{top:21px;font-size:6px;line-height:1.25;color:#b6c1ca}

/* clients */
.clients-title{left:36px;top:845px;font-size:17px}
.round{top:847px;width:20px;height:20px;border-radius:50%;border:1px solid var(--line)}
.card{top:893px;width:151px;height:117px;border:1px solid var(--line);text-align:center}
.card.on{border-bottom:2px solid var(--blue)}
.quote{top:-4px;left:70px;width:12px;height:8px;background:var(--white);color:var(--green-deep);font-size:9px;font-weight:700;line-height:8px}
.card p{font-family:"PT Serif",serif;font-size:6.8px;line-height:1.6;color:#6b7177;padding:14px 17px 0}
.card b{display:block;font-size:5.5px;margin-top:11px;color:var(--ink)}
.card i{display:block;font-size:4.5px;font-style:normal;color:#a5aab0}

/* appointment */
.appt-title{left:36px;top:1040px;font-size:17px}
.field{height:22px;border-bottom:1px solid var(--line);font-size:6px;color:var(--muted);padding:5px 0 0 17px}
.field svg{position:absolute;left:0;top:5px}
.msg{left:364px;top:1076px;width:152px;height:73px;border:1px solid var(--line);font-size:6px;color:var(--muted);padding:6px}
.send{left:36px;top:1161px;width:106px;height:20px;background:var(--blue);color:var(--white);font-size:5.5px;font-weight:700;text-align:center;line-height:20px}

/* contact */
.map{left:0;top:1200px;width:358px;height:167px;background:linear-gradient(160deg,#eceeef,#dfe2e4)}
.pin{left:268px;top:1262px}
.contact{left:358px;top:1200px;width:164px;height:167px;background:var(--blue);color:var(--white);padding:16px 0 0 22px}
.contact h5{font-size:6px;font-weight:700}
.contact p{font-size:6px;line-height:1.5;color:#e0f4fa}
.contact svg{position:absolute;right:26px}
.strip{left:522px;top:1200px;width:27px;height:167px;background:#e4e6e8}

/* footer */
.footer{left:0;top:1367px;width:549px;height:133px;background:var(--slate);color:#d5dde3}
.fcol{top:14px;width:112px}
.fcol h6{font-size:6.5px;font-weight:700;color:var(--white);margin-bottom:9px}
.fcol .tiny{color:#cfd8df}
.fcol .lnk{font-size:5px;line-height:2.45;color:var(--sky)}
.date{font-size:4.5px;color:#a9b5bf}
.news{font-size:5px;line-height:1.5;color:var(--sky);margin-bottom:5px}
.sbox{display:inline-block;width:20px;height:18px;background:var(--slate-light);margin-right:4px;position:relative}
.sbox::after{content:"";position:absolute;left:7px;top:6px;width:6px;height:6px;border-radius:50%;background:#dfe6eb}
.hours{font-size:5px;line-height:2.3;color:var(--white)}
.hours span{float:right;color:#cfd8df}
</style>
</head>
<body>
<div class="stage">
<div class="page">

  <div class="a topbar">
    <span class="a city">Dental &amp; Eye Clinic in Lagos</span>
    <span class="a link" style="left:122px">Email Us</span>
    <span class="a link" style="left:156px">How to Find Us</span>
    <span class="a link" style="left:207px">Give Feedback</span>
    <div class="a" style="left:327px;top:0;width:1px;height:17px;background:var(--line)"></div>
    <span class="a soc" style="left:335px"></span>
    <span class="a soc" style="left:351px"></span>
    <span class="a soc" style="left:367px"></span>
    <span class="a soc" style="left:384px"></span>
    <div class="a search">Search</div>
  </div>

  <div class="a brand"><span class="brand-name">VORANTACARE</span><span class="brand-mark"></span></div>
  <span class="a nav on" style="left:262px">HOME</span>
  <span class="a nav" style="left:298px">ABOUT US ▾</span>
  <span class="a nav" style="left:346px">SERVICES ▾</span>
  <span class="a nav" style="left:393px">BLOG ▾</span>
  <span class="a nav" style="left:427px">PAGES ▾</span>
  <span class="a nav" style="left:465px">CONTACT US</span>

  <div class="a infobar">
    <svg class="a" style="left:36px;top:8px" width="15" height="14" viewBox="0 0 15 14" fill="none" stroke="#1aaed6" stroke-width="1"><circle cx="2" cy="2" r="1.3"/><circle cx="7.5" cy="2" r="1.3"/><circle cx="13" cy="2" r="1.3"/><circle cx="2" cy="7" r="1.3"/><circle cx="7.5" cy="7" r="1.3"/><circle cx="13" cy="7" r="1.3"/><circle cx="2" cy="12" r="1.3"/><circle cx="13" cy="12" r="1.3"/></svg>
    <div class="a t" style="left:63px;top:8px">Call Today 020 4411 2290</div>
    <div class="a s" style="left:63px;top:15px">14 Marina Road, Lagos Island 101241</div>
    <svg class="a" style="left:200px;top:8px" width="13" height="13" viewBox="0 0 13 13" fill="none" stroke="#1aaed6" stroke-width="1"><circle cx="6.5" cy="6.5" r="5.5"/><path d="M6.5 3.5v3h2.5"/></svg>
    <div class="a t" style="left:227px;top:8px">Open Hours</div>
    <div class="a s" style="left:227px;top:15px">Mon - Sat (8 am - 6 pm), Sun CLOSED</div>
  </div>
  <div class="a appt">
    <svg class="a" style="left:12px;top:8px" width="14" height="13" viewBox="0 0 14 13" fill="none" stroke="#fff" stroke-width="1"><rect x=".5" y="1.5" width="13" height="11"/><path d="M.5 4.5h13M3 7h2M6 7h2M9 7h2M3 9.5h2M6 9.5h2"/></svg>
    <div class="a" style="left:39px;top:9px;font-size:5px;font-weight:700">Make an Appointment</div>
    <div class="a" style="left:39px;top:15px;font-size:4.5px;color:#d8f1f9">It's so fast</div>
  </div>

  <div class="a hero" role="img" aria-label="Photo of a clinician in safety glasses examining a young patient"></div>
  <div class="a gear"><svg width="17" height="17" viewBox="0 0 17 17" fill="none" stroke="#fff" stroke-width="1.2"><circle cx="8.5" cy="8.5" r="2"/><circle cx="8.5" cy="8.5" r="4" stroke-dasharray="2 1.2"/></svg></div>
  <div class="a arrow" style="left:0"><svg width="33" height="28" viewBox="0 0 33 28" fill="none" stroke="#fff" stroke-width="1.3"><path d="M19 9l-5 5 5 5"/></svg></div>
  <div class="a arrow" style="left:518px;width:31px"><svg width="31" height="28" viewBox="0 0 31 28" fill="none" stroke="#fff" stroke-width="1.3"><path d="M13 9l5 5-5 5"/></svg></div>
  <div class="a hero-title serif">Eye &amp; Oral Health</div>
  <div class="a hero-sub serif">Consultation for $55</div>
  <div class="a hero-text serif">At our clinic we place emphasis on prevention as well as personalized attention, offering dental, eye and lab services</div>
  <div class="a hero-btn">Read More</div>

  <div class="a tile" style="left:36px;width:158px;background:var(--blue)">
    <h3>Dental Care</h3><p>Implants, braces and whitening for all ages</p>
    <svg width="34" height="42" viewBox="0 0 34 42" fill="none" stroke="#fff" stroke-width="1.3"><path d="M4 9c0-6 8-7 13-4 5-3 13-2 13 4 0 7-4 9-5 13H9C8 18 4 16 4 9z"/><path d="M11 22h12M12 26h10M13 30h8M14 34h6M17 38v2"/></svg>
  </div>
  <div class="a tile green" style="left:194px;width:164px;background:var(--green)">
    <h3>Eye Clinic</h3><p>Eye tests, lenses and eye health for kids and adults</p>
    <svg width="40" height="42" viewBox="0 0 40 42" fill="none" stroke="#3a3f44" stroke-width="1.3"><path d="M2 21c5-8 11-12 18-12s13 4 18 12c-5 8-11 12-18 12S7 29 2 21z"/><circle cx="20" cy="21" r="7"/><circle cx="20" cy="21" r="2.5"/></svg>
  </div>
  <div class="a tile" style="left:358px;width:158px;background:var(--slate)">
    <h3>Medical Laboratory</h3><p>Accurate tests with fast, reliable results</p>
    <svg width="34" height="42" viewBox="0 0 34 42" fill="none" stroke="#fff" stroke-width="1.3"><path d="M12 3h10M14 3v13L4 36c-1 2 0 4 3 4h20c3 0 4-2 3-4L20 16V3"/><path d="M8 28h18"/><circle cx="27" cy="8" r="2"/></svg>
  </div>

  <h2 class="a about-title heading">Abous Us</h2>
  <div class="a about-sub serif">Meet Dr. Adeyemi</div>
  <div class="a photo" role="img" aria-label="Photo of the doctor with a patient in the treatment room"></div>
  <div class="a caption tiny">Dr. Adeyemi with a patient</div>
  <div class="a about-text">
    <p>Our Clinic is dedicated to providing the most up to date general dentistry, eye care and medical laboratory services.</p>
    <p>With two branches in Lagos we offer a world class facility for dental treatment, eye examinations and diagnostic tests.</p>
    <p>We are among the most qualified care providers in Lagos with over 35 years of quality training and experience.</p>
  </div>
  <div class="a cert-panel">
    <h4>Certififcates of<br>completion</h4>
    <div class="a cert" style="top:54px;background:#d8e4f1"></div>
    <div class="a cert" style="top:102px"></div>
    <div class="a cert" style="top:150px;background:#eeeeea"></div>
    <div class="a dot" style="top:108px"></div>
    <div class="a dot" style="top:124px"></div>
  </div>

  <section class="a adv">
    <h2 class="a adv-title heading">Our Advantages</h2>
    <div class="a adv-col" style="left:36px">
      <svg width="34" height="20" viewBox="0 0 34 20" fill="none" stroke="#fff" stroke-width="1"><rect x="3" y=".5" width="28" height="17"/><path d="M.5 19.5h33"/><circle cx="12" cy="7" r="2.5"/><path d="M8 14c0-3 8-3 8 0M19 6h8M19 9h8M19 12h6"/></svg>
      <h4>Accepting Insurance<br>Cards</h4>
      <p>Our clinic can easily accept the customers with insurance cards and create the history of cases for each.</p>
    </div>
    <div class="a adv-col" style="left:159px">
      <svg width="36" height="22" viewBox="0 0 36 22" fill="none" stroke="#fff" stroke-width="1"><circle cx="20" cy="9" r="7"/><circle cx="20" cy="9" r="3"/><circle cx="6" cy="17" r="3"/><circle cx="32" cy="3" r="2"/><path d="M9 16l5-3M26 6l4-2"/></svg>
      <h4>Using Innovative<br>Technology</h4>
      <p>All our dental, eye and lab rooms are furnished with modern equipment kept at the highest standards.</p>
    </div>
    <div class="a adv-col" style="left:282px">
      <svg width="36" height="20" viewBox="0 0 36 20" fill="none" stroke="#fff" stroke-width="1"><path d="M2 5c0-4 6-5 8-2 2-3 8-2 8 2 0 5-3 6-3 12-1 2-3 2-3 0l-2-5-2 5c0 2-3 2-3 0 0-6-3-7-3-12z"/><path d="M18 5c0-4 6-5 8-2 2-3 8-2 8 2 0 5-3 6-3 12-1 2-3 2-3 0l-2-5-2 5c0 2-3 2-3 0 0-6-3-7-3-12z"/></svg>
      <h4>Guarantee Success<br>of Treatments</h4>
      <p>Most of our treatments are covered by a long term guarantee which will be discussed with you before beginning treatment.</p>
    </div>
    <div class="a adv-col" style="left:405px">
      <svg width="36" height="24" viewBox="0 0 36 24" fill="none" stroke="#fff" stroke-width="1"><rect x=".5" y=".5" width="35" height="23"/><rect x="3.5" y="3.5" width="29" height="17"/><circle cx="18" cy="12" r="5"/><circle cx="18" cy="12" r="2.5"/></svg>
      <h4>Certified Dentist<br>&amp; Eye Doctors</h4>
      <p>With over 30 years of experience in dentistry, optometry and lab medicine, we are experts in every field.</p>
    </div>
  </section>

  <section class="a stats">
    <div class="a num" style="left:36px">8</div><div class="a lab" style="left:78px">years<br>of experience</div>
    <div class="a num" style="left:159px">45</div><div class="a lab" style="left:204px">visited<br>conferentions</div>
    <div class="a num" style="left:282px">256</div><div class="a lab" style="left:341px">smiling<br>clients</div>
    <div class="a num" style="left:405px">8</div><div class="a lab" style="left:447px">master<br>certifications</div>
  </section>

  <h2 class="a clients-title heading">Our Happy Clients</h2>
  <div class="a round" style="left:458px"><svg width="18" height="18" viewBox="0 0 18 18" fill="none" stroke="#1aaed6" stroke-width="1.2"><path d="M10 6l-3 3 3 3"/></svg></div>
  <div class="a round" style="left:492px"><svg width="18" height="18" viewBox="0 0 18 18" fill="none" stroke="#1aaed6" stroke-width="1.2"><path d="M8 6l3 3-3 3"/></svg></div>
  <div class="a card" style="left:36px"><span class="a quote">“</span>
    <p>The doctors and nurses and aides were excellent. The food was excellent. I am feeling fine, back to my old self again and it feels great. Thank God for clinics such as yours.</p><b>Tola Benson</b><i>Teacher</i></div>
  <div class="a card" style="left:200px"><span class="a quote">“</span>
    <p>I appreciate all your kindness and good care you gave me. My maintenance treatments have done wonder for me. Thank you so much. Please enjoy the chocolates.</p><b>Ada Nwosu</b><i>Sales Manager</i></div>
  <div class="a card on" style="left:364px"><span class="a quote">“</span>
    <p>Great co workers, really good environment and excellent patient care. They are continuously innovating themselves which is why they remain a premier clinic.</p><b>Femi Lawal</b><i>Handyman</i></div>

  <h2 class="a appt-title heading">Online Appointment</h2>
  <div class="a field" style="left:36px;top:1076px;width:316px">Name
    <svg width="9" height="9" viewBox="0 0 9 9" fill="none" stroke="#1aaed6"><circle cx="4.5" cy="3" r="2"/><path d="M1 8.5c0-3 7-3 7 0"/></svg></div>
  <div class="a field" style="left:36px;top:1103px;width:152px">Phone
    <svg width="9" height="9" viewBox="0 0 9 9" fill="#1aaed6"><rect width="2" height="2"/><rect x="3.5" width="2" height="2"/><rect x="7" width="2" height="2"/><rect y="3.5" width="2" height="2"/><rect x="3.5" y="3.5" width="2" height="2"/><rect x="7" y="3.5" width="2" height="2"/><rect y="7" width="2" height="2"/><rect x="7" y="7" width="2" height="2"/></svg></div>
  <div class="a field" style="left:200px;top:1103px;width:152px">Email
    <svg width="10" height="8" viewBox="0 0 10 8" fill="none" stroke="#1aaed6"><rect x=".5" y=".5" width="9" height="7"/><path d="M.5 .5l4.5 4 4.5-4"/></svg></div>
  <div class="a field" style="left:36px;top:1131px;width:152px">Date
    <svg width="9" height="9" viewBox="0 0 9 9" fill="none" stroke="#1aaed6"><rect x=".5" y=".5" width="8" height="8"/><path d="M.5 3h8M2.5 5h4M2.5 7h4"/></svg></div>
  <div class="a field" style="left:200px;top:1131px;width:152px">Time
    <svg width="9" height="9" viewBox="0 0 9 9" fill="none" stroke="#1aaed6"><circle cx="4.5" cy="4.5" r="4"/><path d="M4.5 2.5v2h2"/></svg></div>
  <div class="a msg">Your message</div>
  <div class="a send">Make an Appointment</div>

  <div class="a map" role="img" aria-label="Street map showing the clinic location in Lagos"></div>
  <svg class="a pin" width="16" height="20" viewBox="0 0 16 20"><path d="M8 20S1 12 1 7.5a7 7 0 0 1 14 0C15 12 8 20 8 20z" fill="#9fbf4a"/><circle cx="8" cy="7.5" r="2.5" fill="#fff"/></svg>
  <div class="a strip"></div>
  <div class="a contact">
    <h5>Office</h5><p>14 Marina Road,<br>Lagos Island 101241</p>
    <svg style="top:16px" width="9" height="11" viewBox="0 0 9 11" fill="none" stroke="#fff"><path d="M4.5 10.5S.5 6 .5 4a4 4 0 0 1 8 0c0 2-4 6.5-4 6.5z"/><circle cx="4.5" cy="4" r="1.4"/></svg>
    <h5 style="margin-top:11px">E-mail</h5><p>service@vorantacare.ng</p>
    <svg style="top:55px" width="10" height="8" viewBox="0 0 10 8" fill="none" stroke="#fff"><rect x=".5" y=".5" width="9" height="7"/><path d="M.5 .5l4.5 4 4.5-4"/></svg>
    <h5 style="margin-top:11px">Phone</h5><p>+234 801 555 0142<br>+234 801 555 0187</p>
    <svg style="top:83px" width="9" height="9" viewBox="0 0 9 9" fill="#fff"><rect width="2" height="2"/><rect x="3.5" width="2" height="2"/><rect x="7" width="2" height="2"/><rect y="3.5" width="2" height="2"/><rect x="3.5" y="3.5" width="2" height="2"/><rect x="7" y="3.5" width="2" height="2"/><rect y="7" width="2" height="2"/><rect x="7" y="7" width="2" height="2"/></svg>
    <h5 style="margin-top:11px">Opening hours</h5><p>Mon - Sat 8.00 - 18.00<br>Sunday CLOSED</p>
    <svg style="top:120px" width="10" height="10" viewBox="0 0 10 10" fill="none" stroke="#fff"><circle cx="5" cy="5" r="4.5"/><path d="M5 2.5v2.5h2"/></svg>
  </div>

  <footer class="a footer">
    <div class="a fcol" style="left:36px">
      <h6>About Us</h6>
      <p class="tiny">We are a highly motivated team, all with very individual qualities and experience, and a high standard of patient care.</p>
      <p class="tiny" style="margin-top:8px">We have advanced training and decades of experience and we constantly strive to provide the best dental, eye and lab care using tried and tested technology.</p>
    </div>
    <div class="a fcol" style="left:159px">
      <h6>Quick Links</h6>
      <div class="lnk">Home<br>About Us<br>Blog<br>FAQ<br>Contact Us<br>Photo Gallery<br>Vacancies<br>Testimonials</div>
    </div>
    <div class="a fcol" style="left:282px">
      <h6>Latest News</h6>
      <div class="date">September 26, 2016</div><div class="news">Our second Lagos branch now offers full eye care</div>
      <div class="date">September 26, 2016</div><div class="news">New laboratory tests now give results on the same day</div>
      <div class="date">September 26, 2016</div><div class="news">If you need a crown or an implant you will pay a fee</div>
    </div>
    <div class="a fcol" style="left:405px">
      <h6>Our Social Pages</h6>
      <div><span class="sbox"></span><span class="sbox"></span><span class="sbox"></span><span class="sbox"></span></div>
      <h6 style="margin-top:14px;margin-bottom:4px">Opening Hours</h6>
      <div class="hours">Monday - Friday <span>9:00 am - 18:00 pm</span><br>Saturday <span>9:00 am - 16:00 pm</span><br>Sunday <span>9:00 am - 14:00 pm</span></div>
    </div>
  </footer>

</div>
</div>
</body>
</html>
```